Online-Marketing Material für einen Online Kurs
Zielgruppe
Online Kurs SerienTitel 'Vom Nebel zum Gipfel' Untertitel: 'Mache aus Deinem schwersten Tag einen Anfang Deiner Stärke!' Zielgruppe: Menschen mit chronischen Rückenschmerzen
Titel: Chronische Rückenschmerzen
Aufgabenstellung
1. Kleine Änderung des Logos: Steady MIndframe raus und Dr. Lukas Brennwald in leuchtendem grün rein
Es gibt zwei Titel: Serientitel und den Kurstitel
2. Logo und Bild für Online Kurs für kursolo und andere Nutzungen, Akzentfarbe soll grün sein. Das Vitabrook Logo kann klein sein, der Titel ist am wichtigsten.
3. Ein Bild sollte für kursolo quadratisch sein.
4. Vielleicht eine Foto Collage von Mensch mit Schmerzen und Mensch mit Power

```html
<!DOCTYPE html>
<html lang="de">
<head>
<meta charset="utf-8">
<title>Vom Nebel zum Gipfel – Chronische Rückenschmerzen</title>
<link href="https://fonts.googleapis.com/css2?family=Roboto:wght@400;500;700;900&family=Kalam:wght@700&display=swap" rel="stylesheet">
<style>
  :root {
    --green: #2ba600;
    --green-bright: #35b81a;
    --white: #ffffff;
    --ink: #333333;
    --logo-grey: #555555;
    --bar-top: #4d4d4d;
    --bar-bottom: #3b3b3b;
  }
  html, body { margin: 0; padding: 0; overflow: hidden; background: var(--white); }
  .canvas {
    position: relative;
    width: 1200px;
    height: 1200px;
    overflow: hidden;
    background: var(--white);
    font-family: "Roboto", Arial, sans-serif;
  }
  .artwork { position: absolute; inset: 0; }
  .series-title {
    position: absolute;
    left: 88px;
    top: 58px;
    margin: 0;
    color: var(--white);
    font-weight: 900;
    line-height: 0.92;
    letter-spacing: -1px;
  }
  .series-title .line-one { display: block; font-size: 88px; }
  .series-title .line-two { display: block; font-size: 112px; }
  .series-subtitle {
    position: absolute;
    left: 88px;
    top: 270px;
    width: 770px;
    margin: 0;
    color: var(--white);
    font-size: 54px;
    font-weight: 400;
    line-height: 1.26;
  }
  .brand {
    position: absolute;
    right: 40px;
    top: 72px;
    text-align: right;
  }
  .brand-name {
    display: block;
    color: var(--logo-grey);
    font-size: 48px;
    font-weight: 500;
    letter-spacing: 1px;
    line-height: 1;
  }
  .brand-person {
    display: block;
    margin-top: 6px;
    color: var(--green-bright);
    font-size: 21px;
    font-weight: 500;
  }
  .course-band {
    position: absolute;
    left: 0; top: 935px;
    width: 1200px; height: 122px;
    background: var(--green);
    display: flex; align-items: center; justify-content: center;
  }
  .course-title {
    margin: 0;
    color: var(--white);
    font-family: "Kalam", "Comic Sans MS", cursive;
    font-weight: 700;
    font-size: 78px;
    line-height: 1;
  }
  .web-bar {
    position: absolute;
    left: 0; top: 1057px;
    width: 1200px; height: 143px;
    background: linear-gradient(180deg, var(--bar-top), var(--bar-bottom));
    display: flex; align-items: center; justify-content: center; gap: 18px;
  }
  .web-address {
    color: var(--white);
    font-size: 36px;
    font-weight: 500;
    letter-spacing: 6px;
  }
</style>
</head>
<body>
<div class="canvas">
  <svg class="artwork" width="1200" height="1200" viewBox="0 0 1200 1200">
    <defs>
      <linearGradient id="officeTones" x1="0" y1="0" x2="1" y2="1">
        <stop offset="0" stop-color="#e9e6e2"/>
        <stop offset="0.5" stop-color="#c9c3bc"/>
        <stop offset="1" stop-color="#8fb2b0"/>
      </linearGradient>
      <radialGradient id="backTones" cx="0.55" cy="0.75" r="0.8">
        <stop offset="0" stop-color="#e6a07a"/>
        <stop offset="0.35" stop-color="#cdb9a1"/>
        <stop offset="1" stop-color="#e8e2da"/>
      </radialGradient>
    </defs>
    <path class="green-field" fill="var(--green)" d="M0,0 H765 C840,100 880,260 870,410 L870,935 L0,935 Z"/>
    <path class="photo-office" role="img" aria-label="Foto: Frau am Schreibtisch mit Laptop, hält sich den schmerzenden Rücken" fill="url(#officeTones)" stroke="var(--white)" stroke-width="14" d="M-10,548 C200,495 470,545 640,720 L640,945 L-10,945 Z"/>
    <path class="photo-back" role="img" aria-label="Foto: Mann im beigen Pullover hält sich den unteren Rücken, Wirbelsäule rot hervorgehoben" fill="url(#backTones)" stroke="var(--white)" stroke-width="14" d="M590,945 C598,760 690,560 830,462 C940,397 1080,377 1210,383 V945 Z"/>
    <g class="pointer-arrow" fill="none" stroke="var(--ink)" stroke-width="6" stroke-linecap="round">
      <path d="M835,228 C905,198 985,235 975,352"/>
      <path d="M952,322 L975,357 L1022,280"/>
    </g>
  </svg>

  <h1 class="series-title">
    <span class="line-one">VOM NEBEL</span>
    <span class="line-two">ZUM GIPFEL</span>
  </h1>
  <p class="series-subtitle">Mache aus Deinem schwersten Tag einen Anfang Deiner Stärke!</p>

  <div class="brand">
    <span class="brand-name">VITABROOK</span>
    <span class="brand-person">Dr. Lukas Brennwald</span>
  </div>

  <div class="course-band">
    <h2 class="course-title">Chronische Rückenschmerzen</h2>
  </div>

  <div class="web-bar">
    <svg class="globe-icon" width="32" height="32" viewBox="0 0 32 32" aria-hidden="true">
      <g fill="none" stroke="var(--green-bright)" stroke-width="2.4">
        <circle cx="16" cy="16" r="13"/>
        <ellipse cx="16" cy="16" rx="6" ry="13"/>
        <path d="M3,16 H29 M5,9 H27 M5,23 H27"/>
      </g>
    </svg>
    <span class="web-address">www.vitabrook.de</span>
  </div>
</div>
</body>
</html>
```